Conference Brochure - VoxLinqera

We are a telephony communications provider that services primarily the automotive industry. The bulk of our products is to provide phone tracking and analytics. See our website for more info on our products!
www.voxlinqera-demo.com
We need a brochure made for future conferences. The brochure style we had in mind in a front and back, three panel brochure. We have all the text ready we want in brochure and know about where we want that text placed. We just need someone to put it together for us!
We want a big brochure. We would prefer each panel to be bigger than a letter size piece of paper.
The brochure needs to look like it is geared towards the automotive industry. It also needs to be easy to read and ascetically pleasing.
I have attached our text for the brochure and our logo.
Thank you!

Target Market(s)

Automotive Industry - Specifically Dealership owners and managers

Industry/Entity Type

Automotive

Font styles to use
Serif
Sans Serif

Requirements
Must have
• The brochure must contain all of the text from the attached document. It must also contain the logo I've attached as well as graphics that seem to go with the automotive industry.
Nice to have
• Pictures of technology or automotive items would be great for graphics.
Should not have
• The brochure cannot contain pictures of specific, recognizable car brands because it will be distributed to many different kinds of dealership owners.

```html
<!DOCTYPE html>
<html lang="en">
<head>
<meta charset="utf-8">
<title>VoxLinqera Conference Brochure</title>
<link href="https://fonts.googleapis.com/css2?family=Oswald:wght@300;400;500;600&family=Open+Sans:ital,wght@0,400;0,600;0,700;1,400&display=swap" rel="stylesheet">
<style>
  :root {
    --navy: #1f3a8a;
    --navy-deep: #1a327a;
    --green: #7cc242;
    --green-soft: #8fcd55;
    --white: #ffffff;
    --ink: #1c1c24;
    --backdrop: #eceae6;
    --photo-warm: #c9a88f;
    --photo-cool: #a9b3c2;
  }
  * { box-sizing: border-box; margin: 0; padding: 0; }
  html, body {
    width: 1200px; height: 697px; overflow: hidden;
    background: var(--backdrop);
    font-family: "Open Sans", Arial, sans-serif;
  }
  .brochure {
    position: absolute; left: 36px; top: 138px;
    width: 1128px; height: 420px;
    display: flex;
    box-shadow: 0 14px 30px rgba(0,0,0,.18);
  }
  .panel { position: relative; width: 376px; height: 420px; overflow: hidden; background: var(--white); }
  .panel + .panel { border-left: 1px solid #e2e2e2; }
  .photo { position: absolute; }

  /* Front cover */
  .cover .photo-team { left: 0; top: 0; width: 206px; height: 196px;
    background: linear-gradient(135deg, var(--photo-cool), var(--photo-warm) 60%, #8a6c58); }
  .cover .photo-agent { left: 212px; top: 0; width: 164px; height: 178px;
    background: linear-gradient(160deg, #f4efe9, var(--photo-warm) 70%, #3b2a24); }
  .cover .divider { position: absolute; left: 206px; top: 0; width: 6px; height: 196px; background: var(--green); }
  .cover .band-blue { position: absolute; left: 0; top: 190px; width: 376px; height: 175px;
    background: var(--navy); clip-path: polygon(0 8%, 100% 0, 100% 100%, 0 100%); }
  .cover .band-green { position: absolute; left: 0; top: 350px; width: 376px; height: 70px;
    background: var(--green); clip-path: polygon(0 22%, 100% 0, 100% 100%, 0 100%); }
  .cover .photo-phone { left: 282px; top: 168px; width: 70px; height: 150px; border-radius: 12px;
    background: linear-gradient(180deg, #f2f2f2, #6b5a4a 55%, #d8d8d8); }
  .cover .headline { position: absolute; left: 22px; top: 232px; font-family: "Oswald", sans-serif; line-height: 1.02; }
  .cover .headline .lead { display: block; color: var(--white); font-weight: 300; font-size: 34px; }
  .cover .headline .key { display: block; color: var(--green); font-weight: 600; font-size: 44px; }
  .cover .headline .tail { display: block; color: var(--white); font-weight: 400; font-size: 31px; }
  .cover .url { position: absolute; left: 24px; bottom: 16px; color: var(--navy-deep);
    font-size: 15px; letter-spacing: 2px; font-weight: 600; }

  /* Back panel with contacts */
  .contact .brand { position: absolute; left: 172px; top: 188px; color: var(--green);
    font-family: "Oswald", sans-serif; font-weight: 500; font-size: 22px; letter-spacing: .5px; }
  .contact .band-blue { position: absolute; left: 0; top: 228px; width: 376px; height: 108px; background: var(--navy); }
  .contact .band-green { position: absolute; left: 0; top: 336px; width: 376px; height: 84px; background: var(--green); }
  .contact .photo-presenter { left: 24px; top: 252px; width: 130px; height: 168px;
    border-radius: 54px 54px 0 0;
    background: linear-gradient(180deg, #b07a52 0%, #e6c5a8 40%, #1d1d22 62%); }
  .contact .details { position: absolute; left: 170px; top: 242px; width: 200px; list-style: none;
    color: var(--white); font-family: "Oswald", sans-serif; font-weight: 300; font-size: 10px; }
  .contact .details li { display: flex; align-items: center; gap: 5px; height: 20px; white-space: nowrap; }
  .contact .details svg { width: 9px; height: 9px; fill: var(--green); flex: none; }

  /* Inside flap */
  .intro .brand { position: absolute; left: 22px; top: 46px; color: var(--green);
    font-family: "Oswald", sans-serif; font-weight: 500; font-size: 40px; letter-spacing: 1px; }
  .intro .band-green { position: absolute; left: 0; top: 118px; width: 376px; height: 170px;
    background: linear-gradient(120deg, var(--green), var(--green-soft)); }
  .intro .band-blue { position: absolute; left: 0; top: 282px; width: 376px; height: 92px;
    background: var(--navy); clip-path: polygon(0 10%, 100% 0, 100% 100%, 0 100%); }
  .intro .photo-consultant { left: 262px; top: 70px; width: 114px; height: 350px;
    border-radius: 48px 48px 0 0;
    background: linear-gradient(180deg, #e8cf8a 0%, #edd3bd 22%, #7b7b80 40%, #5f6066 100%); }
  .intro .headline { position: absolute; left: 24px; top: 162px; width: 228px; font-family: "Oswald", sans-serif; line-height: 1.1; }
  .intro .headline .lead { display: block; color: var(--white); font-weight: 500; font-size: 25px; }
  .intro .headline .mid { display: block; color: var(--white); font-weight: 500; font-size: 22px; }
  .intro .headline .key { display: block; color: var(--navy); font-weight: 500; font-size: 22px; white-space: nowrap; }
  .intro .body { position: absolute; left: 24px; top: 302px; width: 228px; color: var(--white);
    font-style: italic; font-size: 11px; line-height: 1.45; }
  .intro .url { position: absolute; left: 26px; bottom: 16px; color: var(--ink);
    font-size: 12px; letter-spacing: 2.5px; font-weight: 600; }
</style>
</head>
<body>
<main class="brochure">

  <section class="panel cover">
    <div class="photo photo-team" role="img" aria-label="Smiling support agent with headset in front of business team"></div>
    <div class="divider"></div>
    <div class="photo photo-agent" role="img" aria-label="Smiling customer service agent wearing a headset"></div>
    <div class="band-blue"></div>
    <div class="band-green"></div>
    <div class="photo photo-phone" role="img" aria-label="Smartphone showing a website"></div>
    <h1 class="headline">
      <span class="lead">Grow your</span>
      <span class="key">Dealership,</span>
      <span class="tail">not your budget</span>
    </h1>
    <p class="url">www.voxlinqera-demo.com</p>
  </section>

  <section class="panel contact">
    <p class="brand">VoxLinqera</p>
    <div class="band-blue"></div>
    <div class="band-green"></div>
    <div class="photo photo-presenter" role="img" aria-label="Businesswoman in a dark suit presenting with open hand"></div>
    <ul class="details">
      <li><svg viewBox="0 0 10 10"><path d="M5 0a3.5 3.5 0 0 0-3.5 3.5C1.5 6 5 10 5 10s3.5-4 3.5-6.5A3.5 3.5 0 0 0 5 0zm0 5a1.5 1.5 0 1 1 0-3 1.5 1.5 0 0 1 0 3z"/></svg>4820 Harlow Ridge Dr Ste 300 - Brenmoor, TX 75012</li>
      <li><svg viewBox="0 0 10 10"><path d="M2 0l2 2.5-1 1.2a6 6 0 0 0 3.3 3.3l1.2-1L10 8l-1.5 2C4 10 0 6 0 1.5z"/></svg>1-800-555-0142</li>
      <li><svg viewBox="0 0 10 10"><path d="M0 2h10v6H0zm1 1v.3l4 2.5 4-2.5V3z"/></svg>sales@voxlinqera-demo.com</li>
      <li><svg viewBox="0 0 10 10"><path d="M5 0a5 5 0 1 0 0 10A5 5 0 0 0 5 0zm0 1.2c.7.8 1.2 2 1.3 3.3H3.7C3.8 3.2 4.3 2 5 1.2zM3.7 5.5h2.6C6.2 6.8 5.7 8 5 8.8 4.3 8 3.8 6.8 3.7 5.5z"/></svg>www.voxlinqera-demo.com</li>
    </ul>
  </section>

  <section class="panel intro">
    <p class="brand">VoxLinqera</p>
    <div class="band-green"></div>
    <div class="band-blue"></div>
    <div class="photo photo-consultant" role="img" aria-label="Confident businesswoman in grey blazer with arms crossed"></div>
    <h2 class="headline">
      <span class="lead">Top Notch Support</span>
      <span class="mid">to make your</span>
      <span class="key">EXPERIENCE WONDERFUL</span>
    </h2>
    <p class="body">We are a telephony communications provider that services primarily the automotive industry. The bulk of our products is to provide phone tracking and analytics.</p>
    <p class="url">www.voxlinqera-demo.com</p>
  </section>

</main>
</body>
</html>
```